A UK based Lettings and Property Management Company - Brindle Oak Property

Brindle Oak Property rents and manages properties on behalf of owners in Liverpool, UK. We are looking for a clean, fresh modern design which incororates our logo.

In terms of pages we initially require:

Home
Lettings
Property Management
Landlords
Tenants
About
Contact

In would like to use colours compatible with the logo

Target Market(s)

People looking to rent property
Owners looking to use our services to let their property

Industry/Entity Type

Property

Contact Information for Business Card

Logo prominent on one side
Address to be edited by us as we are moving premises in October
Name Gareth Whitlow
Tel number 0151 486 2037
e-mail gareth@brindleoakhomes.co.uk

Font styles to use
Sans Serif

Colors

Designer to choose colors to be used in the design.

Requirements
Must have
• Clean lines
• Fresh
• Easy navigation
• Easy editing
• Data capture

```html
<!DOCTYPE html>
<html lang="en">
<head>
<meta charset="utf-8">
<title>Brindle Oak Property – Lettings &amp; Property Management</title>
<link rel="stylesheet" href="https://fonts.googleapis.com/css2?family=Montserrat:wght@600;700&family=Source+Sans+3:wght@300;400;600;700&display=swap">
<style>
:root{
  --blue:#1fa4ea;
  --orange:#f3a712;
  --navy:#0f1c3f;
  --footer:#2a3349;
  --red:#e4243a;
  --green:#62c40c;
  --dark-badge:#333;
  --text:#333;
  --page:#f5f6f8;
  --field-border:#d5d8dc;
}
*{box-sizing:border-box;margin:0;padding:0}
html,body{width:758px;height:1200px;overflow:hidden}
body{position:relative;background:var(--page);font-family:"Source Sans 3",Arial,sans-serif;color:var(--text)}
.abs{position:absolute}

.hero{left:0;top:0;width:758px;height:319px;background:linear-gradient(180deg,#1d2a44 0%,#2b3a58 40%,#3a4a63 70%,#26324a 100%)}
.hero-shade{left:0;top:0;width:758px;height:48px;background:rgba(20,30,55,.45)}
.brand{left:76px;top:10px;height:29px;display:flex;align-items:center;gap:6px}
.brand-mark{width:22px;height:22px;background:#fff}
.brand-name{color:#fff;font-weight:700;font-size:13px;letter-spacing:.3px;white-space:nowrap}
.nav{top:18px;left:296px;width:318px;display:flex;justify-content:space-between}
.nav a{color:#fff;font-size:7px;font-weight:400;text-decoration:none;letter-spacing:.2px;white-space:nowrap;line-height:9px}
.btn{background:var(--blue);color:#fff;font-size:7px;display:flex;align-items:center;justify-content:center;text-transform:uppercase;letter-spacing:.2px;white-space:nowrap}
.signin{left:630px;top:13px;width:53px;height:19px}
.hero-title{left:0;width:758px;top:146px;text-align:center;color:#fff;font-weight:700;font-size:18px;letter-spacing:.2px;line-height:22px}
.hero-title span{color:var(--orange)}
.hero-sub{left:0;width:758px;top:174px;text-align:center;color:#fff;font-size:9px;line-height:11px}

.tab{top:245px;height:26px;color:#fff;font-size:8px;display:flex;align-items:center;justify-content:center}
.tab-buy{left:76px;width:57px;background:#8a8d93}
.tab-rent{left:134px;width:60px;background:var(--orange)}
.search{left:76px;top:271px;width:606px;height:97px;background:#fff;box-shadow:0 2px 6px rgba(0,0,0,.08)}
.field{position:absolute;height:23px;border:1px solid var(--field-border);font-size:7.5px;color:#555;display:flex;align-items:center;padding-left:5px;white-space:nowrap}
.field.select::after{content:"";position:absolute;right:5px;top:8px;border:2px solid transparent;border-bottom:2.5px solid #555;border-top:0}
.field.select::before{content:"";position:absolute;right:5px;top:12px;border:2px solid transparent;border-top:2.5px solid #555;border-bottom:0}
.field.text{padding-left:8px;color:#777}
.search-btn{position:absolute;right:0;top:0;width:88px;height:97px;background:var(--blue);color:#fff;display:flex;flex-direction:column;align-items:center;justify-content:center;gap:6px;font-size:7.5px;font-weight:700}

.sec-title{left:0;width:758px;top:421px;text-align:center;font-family:Montserrat,Arial,sans-serif;font-weight:700;font-size:15px;color:var(--navy)}
.sec-sub{left:0;width:758px;top:446px;text-align:center;font-size:8px;color:#444}
.sec-line{left:366px;top:462px;width:26px;height:1px;background:var(--blue)}

.card{position:absolute;width:192px;height:248px;background:#fff}
.card-img{position:absolute;left:0;top:0;width:192px;height:155px}
.price{position:absolute;right:0;top:131px;height:24px;background:var(--orange);color:#fff;font-size:10px;display:flex;align-items:center;padding:0 10px;white-space:nowrap}
.price sup{font-size:6px;margin-right:1px}
.price small{font-size:7px;margin-top:4px}
.badges{position:absolute;left:10px;top:167px;display:flex;gap:3px}
.badge{height:11px;padding:0 5px;color:#fff;font-size:4.5px;display:flex;align-items:center;text-transform:uppercase;white-space:nowrap}
.sale{background:var(--red)}.rent{background:var(--green)}.hot{background:var(--dark-badge)}
.card h3{position:absolute;left:10px;top:183px;font-size:10px;font-weight:700;color:#222;white-space:nowrap}
.addr{position:absolute;left:10px;top:198px;font-size:7px;color:#555;white-space:nowrap}
.card hr{position:absolute;left:10px;top:213px;width:172px;border:0;border-top:1px solid #e6e6e6}
.area{position:absolute;left:10px;top:221px;font-size:7px;color:#555}
.feats{position:absolute;right:17px;top:220px;display:flex;gap:6px;font-size:7px;color:#555;align-items:center}
.feats span{display:flex;align-items:center;gap:3px}
.feats svg{width:9px;height:8px}
.card.raised{box-shadow:0 3px 6px rgba(0,0,0,.12)}

.view-all{left:326px;top:1044px;width:104px;height:26px}
.cta{left:0;top:1108px;width:758px;height:92px;background:var(--footer)}
.cta-text{left:75px;top:1143px;color:#fff;font-size:15px;font-weight:300;white-space:nowrap}
.cta-text span{color:var(--orange)}
.contact-btn{left:610px;top:1140px;width:72px;height:26px}
</style>
</head>
<body>
<svg width="0" height="0" style="position:absolute">
  <defs>
    <symbol id="i-bed" viewBox="0 0 12 9"><rect x="0" y="1" width="1.5" height="8" fill="#1fa4ea"/><rect x="0" y="5" width="12" height="2" fill="#1fa4ea"/><rect x="10.5" y="5" width="1.5" height="4" fill="#1fa4ea"/><rect x="2" y="3" width="3" height="2" fill="#1fa4ea"/><rect x="5.5" y="3.5" width="6.5" height="1.5" fill="#1fa4ea"/></symbol>
    <symbol id="i-bath" viewBox="0 0 12 9"><path d="M1 0h2v4H1z M0 4h12v2a3 3 0 0 1-3 3H3a3 3 0 0 1-3-3z" fill="#1fa4ea"/></symbol>
    <symbol id="i-car" viewBox="0 0 12 9"><path d="M2 3l1.5-3h5L10 3h1.5v4h-11V3z" fill="#1fa4ea"/><circle cx="3" cy="7.5" r="1.5" fill="#1fa4ea"/><circle cx="9" cy="7.5" r="1.5" fill="#1fa4ea"/><rect x="3.8" y="1" width="4.4" height="2" fill="#fff"/></symbol>
  </defs>
</svg>

<div class="abs hero" role="img" aria-label="Evening photograph of a modern glass-walled house with garden"></div>
<div class="abs hero-shade"></div>
<div class="abs brand"><div class="brand-mark"></div><div class="brand-name">BRINDLE OAK PROPERTY</div></div>
<nav class="abs nav">
  <a>HOME</a><a>LETTINGS</a><a>PROPERTY MANAGEMENT</a><a>LANDLORDS</a><a>TENANTS</a><a>ABOUT</a><a>CONTACT</a>
</nav>
<div class="abs btn signin">Sign in</div>
<h1 class="abs hero-title">QUALITY HOMES <span>TO LET</span></h1>
<p class="abs hero-sub">Liverpool lettings &amp; property management specialists</p>

<div class="abs tab tab-buy">Buy</div>
<div class="abs tab tab-rent">Rent</div>
<form class="abs search">
  <div class="field text" style="left:18px;top:16px;width:108px">Street, town &amp; landmark</div>
  <div class="field select" style="left:141px;top:16px;width:108px">Location</div>
  <div class="field select" style="left:264px;top:16px;width:108px">Property status</div>
  <div class="field select" style="left:387px;top:16px;width:107px">All property types</div>
  <div class="field select" style="left:18px;top:56px;width:66px">Bedroom</div>
  <div class="field select" style="left:100px;top:56px;width:66px">Bathroom</div>
  <div class="field select" style="left:182px;top:56px;width:66px">Min price</div>
  <div class="field select" style="left:264px;top:56px;width:66px">Max price</div>
  <div class="field select" style="left:346px;top:56px;width:66px">Min area</div>
  <div class="field select" style="left:428px;top:56px;width:66px">Max area</div>
  <div class="search-btn">
    <svg width="28" height="28" viewBox="0 0 28 28"><circle cx="11" cy="11" r="9" fill="none" stroke="#fff" stroke-width="2"/><path d="M6 10a5 5 0 0 1 5-5" fill="none" stroke="#fff" stroke-width="1.3"/><path d="M18 18l7 7" stroke="#fff" stroke-width="3" stroke-linecap="round"/></svg>
    SEARCH
  </div>
</form>

<h2 class="abs sec-title">WHAT’S NEW ON THE MARKET</h2>
<p class="abs sec-sub">Check out some of our listed properties</p>
<div class="abs sec-line"></div>

<article class="card" style="left:75px;top:494px">
  <div class="card-img" role="img" aria-label="Bright white kitchen with island" style="background:linear-gradient(160deg,#e9eaec,#cfd3d6 60%,#eef0f0)"></div>
  <div class="price"><sup>$</sup>650.000</div>
  <div class="badges"><span class="badge sale">For sale</span><span class="badge hot">Hot offer</span></div>
  <h3>The Chalet Estate</h3>
  <p class="addr">L17 4QW Calder Mews, Liverpool, United Kingdom</p><hr>
  <p class="area">Area : 3578 Sqft</p>
  <div class="feats"><span><svg><use href="#i-bed"/></svg>03</span><span><svg><use href="#i-bath"/></svg>02</span><span><svg><use href="#i-car"/></svg>Yes</span></div>
</article>

<article class="card" style="left:283px;top:494px">
  <div class="card-img" role="img" aria-label="Open plan living room and kitchen" style="background:linear-gradient(160deg,#d9d8d3,#b7b3aa 55%,#e4e3df)"></div>
  <div class="price"><sup>$</sup>4800.00<small>/Mon</small></div>
  <div class="badges"><span class="badge rent">For rent</span></div>
  <h3>Morden Apartment</h3>
  <p class="addr">L17 4QW Calder Mews, Liverpool, United Kingdom</p><hr>
  <p class="area">Area : 3578 Sqft</p>
  <div class="feats"><span><svg><use href="#i-bed"/></svg>03</span><span><svg><use href="#i-bath"/></svg>02</span><span><svg><use href="#i-car"/></svg>Yes</span></div>
</article>

<article class="card" style="left:490px;top:494px">
  <div class="card-img" role="img" aria-label="White lounge with staircase and wooden floor" style="background:linear-gradient(160deg,#e4e2dc,#c9c2b4 60%,#b89a72)"></div>
  <div class="price"><sup>$</sup>4800.00<small>/Mon</small></div>
  <div class="badges"><span class="badge rent">For rent</span><span class="badge hot">Hot offer</span></div>
  <h3>Luxurious Deplux</h3>
  <p class="addr">L17 4QW Calder Mews, Liverpool, United Kingdom</p><hr>
  <p class="area">Area : 3578 Sqft</p>
  <div class="feats"><span><svg><use href="#i-bed"/></svg>03</span><span><svg><use href="#i-bath"/></svg>02</span><span><svg><use href="#i-car"/></svg>Yes</span></div>
</article>

<article class="card" style="left:75px;top:758px">
  <div class="card-img" role="img" aria-label="Living room with sofa and dining area" style="background:linear-gradient(160deg,#d8d3c8,#b3a895 60%,#8d7a62)"></div>
  <div class="price"><sup>$</sup>650.00</div>
  <div class="badges"><span class="badge sale">For sale</span></div>
  <h3>Westbourne House</h3>
  <p class="addr">L17 4QW Calder Mews, Liverpool, United Kingdom</p><hr>
  <p class="area">Area : 3578 Sqft</p>
  <div class="feats"><span><svg><use href="#i-bed"/></svg>03</span><span><svg><use href="#i-bath"/></svg>02</span><span><svg><use href="#i-car"/></svg>Yes</span></div>
</article>

<article class="card raised" style="left:283px;top:758px">
  <div class="card-img" role="img" aria-label="White sitting room with tall windows" style="background:linear-gradient(160deg,#eeeeec,#cfcdc7 55%,#9c9a94)"></div>
  <div class="price"><sup>$</sup>650.00</div>
  <div class="badges"><span class="badge sale">For sale</span></div>
  <h3>Sturrock Place Gordon</h3>
  <p class="addr">L17 4QW Calder Mews, Liverpool, United Kingdom</p><hr>
  <p class="area">Area : 3578 Sqft</p>
  <div class="feats"><span><svg><use href="#i-bed"/></svg>03</span><span><svg><use href="#i-bath"/></svg>02</span><span><svg><use href="#i-car"/></svg>Yes</span></div>
</article>

<article class="card" style="left:490px;top:758px">
  <div class="card-img" role="img" aria-label="Modern lounge with warm ceiling lights and kitchen" style="background:linear-gradient(160deg,#e6dfc9,#c8c4b8 50%,#8e8d89)"></div>
  <div class="price"><sup>$</sup>4800.00<small>/Mon</small></div>
  <div class="badges"><span class="badge rent">For rent</span><span class="badge hot">Hot offer</span></div>
  <h3>Valmark Orchard</h3>
  <p class="addr">L17 4QW Calder Mews, Liverpool, United Kingdom</p><hr>
  <p class="area">Area : 3578 Sqft</p>
  <div class="feats"><span><svg><use href="#i-bed"/></svg>03</span><span><svg><use href="#i-bath"/></svg>02</span><span><svg><use href="#i-car"/></svg>Yes</span></div>
</article>

<div class="abs btn view-all">View all properties</div>

<section class="abs cta"></section>
<p class="abs cta-text">Would you like a free price history graph <span>for your area?</span></p>
<div class="abs btn contact-btn">Contact us</div>
</body>
</html>
```